Kestrel Valley Alpine Riders Society needs a business card design

We need a business card design for our newly incorporated KVARS. We are helping the NZ Chinese community, as well as everyone else, to organise ski & snowboarding trips, training, and equipments. The design should be creative, energetic, young and vibrant.

Industry/Entity Type

Social Club

Contact Information for Business Card

Logo; Kestrel Valley Alpine Riders Society; Name: Oliver Brandt; Position: President; Address: 42 Marwick Rd, Epsom, Auckland 1051; Mobile: 020 7826 1957; Email: oliver@kvars-club.example; Web: www.kvars-club.example

Requirements
Must have
• 1, The text "Kestrel Valley Alpine Riders Society" should be put together with the supplied logo file to form a new complete logo combination.
• 2, Final design files should be in Adobe Illustrator format and all text must be editable.
Nice to have
• two or three colours

```html
<!DOCTYPE html>
<html lang="en">
<head>
<meta charset="utf-8">
<title>KVARS Business Card – Oliver Brandt</title>
<link href="https://fonts.googleapis.com/css2?family=Arimo:wght@400&display=swap" rel="stylesheet">
<style>
  :root {
    --navy: #0b1a8e;
    --green: #2cf01c;
    --ice: #5cc6f2;
    --ink: #111111;
    --paper: #ffffff;
    --rule: #222222;
  }
  html, body {
    margin: 0;
    padding: 0;
    width: 1200px;
    height: 688px;
    overflow: hidden;
    background: var(--paper);
  }
  .card {
    position: relative;
    width: 1200px;
    height: 688px;
    box-sizing: border-box;
    border: 2px solid var(--ink);
    background: var(--paper);
    overflow: hidden;
    font-family: "Arimo", Arial, sans-serif;
    font-weight: 400;
  }
  .card__shapes {
    position: absolute;
    inset: 0;
    width: 1200px;
    height: 688px;
  }
  .brand {
    position: absolute;
    left: 68px;
    top: 22px;
    display: flex;
    flex-direction: column;
    align-items: flex-start;
  }
  .brand__row {
    display: flex;
    align-items: center;
    gap: 14px;
  }
  .brand__dot {
    width: 34px;
    height: 34px;
    border-radius: 50%;
    background: var(--ice);
  }
  .brand__name {
    font-size: 98px;
    line-height: 1;
    color: var(--navy);
    letter-spacing: 2px;
  }
  .brand__tagline {
    margin-top: 10px;
    font-size: 14px;
    color: var(--navy);
    white-space: nowrap;
  }
  .person {
    position: absolute;
    left: 0;
    width: 500px;
    top: 262px;
    text-align: center;
    color: var(--navy);
  }
  .person__name {
    margin: 0;
    font-size: 56px;
    line-height: 1.1;
    font-weight: 400;
    text-transform: uppercase;
  }
  .person__role {
    margin: 8px 0 0;
    font-size: 54px;
    line-height: 1.1;
    text-transform: uppercase;
  }
  .divider {
    position: absolute;
    left: 502px;
    top: 202px;
    width: 2px;
    height: 218px;
    background: var(--rule);
  }
  .contact {
    position: absolute;
    left: 636px;
    color: var(--ink);
    font-size: 46px;
    line-height: 1;
    white-space: nowrap;
  }
  .contact--phone { top: 188px; font-size: 50px; }
  .contact--email { top: 272px; font-size: 38px; }
  .contact--address { top: 348px; line-height: 1.2; font-size: 46px; }
  .icon {
    position: absolute;
    fill: var(--navy);
  }
</style>
</head>
<body>
  <div class="card">
    <svg class="card__shapes" viewBox="0 0 1200 688" aria-hidden="true">
      <polygon class="corner-band" points="0,0 574,0 426,170 0,170" fill="var(--green)"/>
      <rect class="footer-band" x="0" y="545" width="1200" height="143" fill="var(--navy)"/>
      <polygon class="footer-stripe" points="369,545 665,545 784,688 489,688" fill="var(--green)"/>
    </svg>

    <div class="brand">
      <div class="brand__row">
        <span class="brand__dot"></span>
        <span class="brand__name">KVARS</span>
      </div>
      <span class="brand__tagline">Kestrel Valley Alpine Riders Society</span>
    </div>

    <div class="person">
      <h1 class="person__name">Oliver Brandt</h1>
      <p class="person__role">President</p>
    </div>

    <div class="divider"></div>

    <svg class="icon icon--phone" style="left:545px;top:186px" width="46" height="42" viewBox="0 0 24 24" aria-hidden="true">
      <path d="M6.6 10.8c1.4 2.8 3.8 5.1 6.6 6.6l2.2-2.2c.3-.3.7-.4 1-.2 1.1.4 2.3.6 3.6.6.6 0 1 .4 1 1V20c0 .6-.4 1-1 1C10.6 21 3 13.4 3 4c0-.6.4-1 1-1h3.5c.6 0 1 .4 1 1 0 1.3.2 2.5.6 3.6.1.3 0 .7-.2 1z"/>
    </svg>
    <svg class="icon icon--mail" style="left:537px;top:268px" width="60" height="38" viewBox="0 0 60 38" aria-hidden="true">
      <path d="M0 0h60v5L30 22 0 5z"/>
      <path d="M0 10l30 17 30-17v28H0z"/>
    </svg>
    <svg class="icon icon--pin" style="left:540px;top:352px" width="58" height="76" viewBox="0 0 58 76" aria-hidden="true">
      <path d="M29 2C17 2 8 11 8 23c0 15 21 37 21 37s21-22 21-37C50 11 41 2 29 2zm0 30a9 9 0 1 1 0-18 9 9 0 0 1 0 18z"/>
      <path d="M29 76C13 76 2 72 2 67c0-3 4-5 10-6.5l2 3C9 64.5 8 66 8 67c0 2 8 4 21 4s21-2 21-4c0-1-1-2.5-6-3.5l2-3c6 1.5 10 3.5 10 6.5 0 5-11 9-27 9z"/>
    </svg>

    <div class="contact contact--phone">020 7826 1957</div>
    <div class="contact contact--email">oliver@kvars-club.example</div>
    <div class="contact contact--address">42 Marwick Rd, Epsom<br>Auckland 1051</div>
  </div>
</body>
</html>
```